Banner Pop Up Opt In Form REDESIGNS - SLEEK BLACK LOOK

Please redesign banners attached.

I am looking for a very sleek look....I do not like this collage of images on these current designs. Please keep all content same but use images that pop.

I have an acccount at www.pixmorrow-example.com or you can use your own images.

I like black background for somereason because it looks very sleek....but these designs should pop , build trust and credibility and have easy opt in form....SLEEK AND MODERN LOOK is what im looking for....

Target Market(s)

Consumers on websites

Requirements
Must have
• Please redesign banners attached.

Nice to have

Should not have

```html
<!DOCTYPE html>
<html lang="en">
<head>
<meta charset="utf-8">
<title>Newsletter Opt-In Banner – Smart Fitness Watch</title>
<link rel="stylesheet" href="https://fonts.googleapis.com/css2?family=Montserrat:wght@400;500;800&family=Poppins:wght@300;400&display=swap">
<style>
  :root {
    --black: #000000;
    --orange: #f8a01f;
    --white: #ffffff;
    --field-line: #c8c8c8;
    --placeholder: #8a8a8a;
    --page: #ffffff;
    --photo-light: #fbf3df;
    --photo-warm: #e8c48a;
    --photo-mid: #c9a078;
    --photo-blue: #4aa3d8;
  }
  * { margin: 0; padding: 0; box-sizing: border-box; }
  html, body {
    width: 1200px; height: 1200px; overflow: hidden;
    background: var(--page);
  }
  .banner {
    position: absolute; left: 60px; top: 60px;
    width: 1080px; height: 1080px;
    overflow: hidden;
    background: var(--black);
    box-shadow: 0 0 40px rgba(0,0,0,0.18);
  }
  .backdrop { position: absolute; inset: 0; }
  .headline {
    position: absolute; left: 57px; top: 80px;
    font-family: "Montserrat", sans-serif; font-weight: 800;
    font-size: 58px; line-height: 76px; letter-spacing: -1px;
    color: var(--white);
  }
  .headline .accent { color: var(--orange); display: block; }
  .intro {
    position: absolute; left: 57px; top: 236px;
    font-family: "Montserrat", sans-serif; font-weight: 400;
    font-size: 22px; line-height: 30px; color: var(--white);
  }
  .product-photo {
    position: absolute; left: 55px; top: 321px;
    width: 190px; height: 240px;
    background: radial-gradient(ellipse at 50% 45%, #4a4a4a 0%, #262626 55%, #0d0d0d 100%);
    border-radius: 28px;
  }
  .product-name {
    position: absolute; left: 274px; top: 346px;
    font-family: "Montserrat", sans-serif; font-weight: 800;
    font-size: 46px; line-height: 62px; letter-spacing: -0.5px;
    color: var(--white);
  }
  .product-name .accent { color: var(--orange); }
  .optin-form { position: absolute; left: 74px; top: 652px; width: 366px; }
  .field {
    display: block; height: 63px;
    border-bottom: 2px solid var(--field-line);
    padding: 10px 0 0 4px;
    font-family: "Poppins", sans-serif; font-weight: 300;
    font-size: 21px; color: var(--placeholder);
  }
  .field:first-child { height: 49px; padding-top: 0; }
  .submit {
    position: absolute; left: 3px; top: 218px;
    width: 118px; height: 34px; border-radius: 17px;
    background: var(--orange); color: var(--white);
    font-family: "Poppins", sans-serif; font-weight: 400;
    font-size: 22px; line-height: 34px; text-align: center;
  }
  .footnote {
    position: absolute; left: 68px; top: 1015px;
    font-family: "Poppins", sans-serif; font-weight: 300;
    font-size: 13px; line-height: 15px; color: var(--white);
  }
  .footnote span { display: block; padding-left: 6px; }
</style>
</head>
<body>
<div class="banner">
  <svg class="backdrop" viewBox="0 0 1080 1080" width="1080" height="1080">
    <defs>
      <linearGradient id="sunlit" x1="0" y1="0" x2="1" y2="1">
        <stop offset="0" stop-color="var(--photo-light)"/>
        <stop offset="0.45" stop-color="var(--photo-warm)"/>
        <stop offset="1" stop-color="var(--photo-mid)"/>
      </linearGradient>
    </defs>
    <g role="img" aria-label="Photo of a woman runner in a blue tank top looking out over a sunlit city riverside">
      <rect x="400" y="0" width="680" height="1080" fill="url(#sunlit)"/>
      <rect x="720" y="440" width="300" height="560" rx="60" fill="var(--photo-blue)" opacity="0.55"/>
    </g>
    <path class="wave-orange" fill="var(--orange)"
      d="M0 0 H608 C660 90 690 220 678 313 C668 420 660 480 617 562 C580 640 530 690 518 748 C500 820 495 880 511 935 C530 1000 570 1050 612 1080 H0 Z"/>
    <path class="wave-black" fill="var(--black)"
      d="M0 0 H502 C590 110 648 220 642 325 C636 470 580 650 524 748 C470 860 446 960 443 1080 H0 Z"/>
  </svg>

  <h1 class="headline">WANT A<span class="accent">GREAT OFFER?</span></h1>
  <p class="intro">SUBSCRIBE TO OUR NEWSLETTER AND<br>RECIEVE COMPLEMENTARY</p>

  <div class="product-photo" role="img" aria-label="Product photo of a black smart fitness watch showing a step count"></div>
  <h2 class="product-name">SMART<br>FITNESS<br><span class="accent">WATCH</span></h2>

  <div class="optin-form">
    <span class="field">Name</span>
    <span class="field">Email</span>
    <span class="field">Phone</span>
    <span class="submit">Submit</span>
  </div>

  <p class="footnote">*we will send an email and a text message with the<span>offer and instructions on how to redeem</span></p>
</div>
</body>
</html>
```